Quarry Lane Co. needs Business Cards

For this project, we need business cards (currently have also put a call out for a logo). We are a start-up called Quarry Lane Co. This is our second company (our first one was called Brightwickery). Traditionally we have been providing market research services across different sectors, primarily financial services and the pharmaceutical industry. However, we now want to go beyond market research to offer more (Etc.)... strategic consulting and big data knowledge management. We want our brand to be approachable, creative, fun but professional.

Target Market(s)

The target audience is a business professional - we are B2B (business to business) and do not sell our services to individuals. The brands we work with are major brands across industries, but primarily automotive, financial and pharmaceutical.

Industry/Entity Type

Market Research

Font styles to use
Serif
Sans Serif
Other font styles liked:
• Calibri

Requirements
Must have
• Be clean, simple, modern
Show our address and phone number and email address and website URL
We do not need to have titles showing.

```html
<!DOCTYPE html>
<html lang="en">
<head>
<meta charset="utf-8">
<title>Quarry Lane Co. — Business Cards</title>
<link href="https://fonts.googleapis.com/css2?family=Open+Sans:wght@400;600&display=swap" rel="stylesheet">
<style>
  :root {
    --teal: #13ad9d;
    --white: #ffffff;
    --ink: #2b2b2b;
    --backdrop: #e9ecec;
  }
  html, body {
    margin: 0;
    padding: 0;
    overflow: hidden;
  }
  body {
    width: 1200px;
    height: 676px;
    background: var(--backdrop);
    font-family: "Open Sans", Calibri, sans-serif;
    display: flex;
    align-items: center;
    justify-content: center;
    gap: 40px;
  }
  .card {
    position: relative;
    width: 540px;
    height: 310px;
    overflow: hidden;
    box-shadow: 0 6px 18px rgba(0,0,0,0.18);
  }
  .card-back {
    background: var(--teal);
  }
  .card-back .brand-name {
    position: absolute;
    right: 52px;
    bottom: 66px;
    color: var(--white);
    font-size: 22px;
    font-weight: 400;
  }
  .card-front {
    background: var(--white);
  }
  .header-band {
    position: absolute;
    left: 0;
    top: 22px;
    width: 100%;
    height: 100px;
    background: var(--teal);
  }
  .header-band .brand-name {
    position: absolute;
    left: 150px;
    top: 38px;
    color: var(--white);
    font-size: 28px;
    font-weight: 400;
  }
  .rule {
    position: absolute;
    left: 30px;
    top: 132px;
    width: 480px;
    height: 2px;
    background: var(--teal);
  }
  .contact-list {
    position: absolute;
    left: 30px;
    top: 144px;
    margin: 0;
    padding: 0;
    list-style: none;
    font-size: 12.5px;
    color: var(--ink);
    line-height: 17px;
  }
  .contact-list li {
    display: flex;
    align-items: center;
    gap: 8px;
  }
  .contact-list svg { width: 10px; height: 10px; flex: none; }
  .address {
    position: absolute;
    right: 30px;
    top: 178px;
    text-align: right;
    font-size: 12.5px;
    color: var(--ink);
    line-height: 17px;
    display: flex;
    align-items: flex-end;
    gap: 8px;
  }
  .address svg { width: 10px; height: 13px; margin-bottom: 2px; flex: none; }
  .footer-band {
    position: absolute;
    left: 0;
    bottom: 0;
    width: 540px;
    height: 70px;
  }
</style>
</head>
<body>
  <section class="card card-back" aria-label="Card back">
    <span class="brand-name">Quarry Lane Co.</span>
  </section>

  <section class="card card-front" aria-label="Card front">
    <svg class="footer-band" viewBox="0 0 540 70" aria-hidden="true">
      <path d="M0 14 Q270 62 540 50 L540 70 L0 70 Z" fill="var(--teal)"/>
    </svg>

    <div class="header-band">
      <span class="brand-name">Quarry Lane Co.</span>
    </div>

    <div class="rule"></div>

    <ul class="contact-list">
      <li>
        <svg viewBox="0 0 10 10" aria-hidden="true"><path d="M2 1 L4 1 L4.6 3 L3.4 3.8 Q4.4 5.8 6.2 6.6 L7 5.4 L9 6 L9 8 Q5 9 1.5 4.5 Q1 2.5 2 1 Z" fill="var(--teal)"/></svg>
        <span>0123 456 789</span>
      </li>
      <li>
        <svg viewBox="0 0 10 10" aria-hidden="true"><rect x="1" y="1" width="8" height="8" fill="none" stroke="var(--teal)" stroke-width="1.2"/></svg>
        <span>0123 456 789</span>
      </li>
      <li>
        <svg viewBox="0 0 10 10" aria-hidden="true"><rect x="0.5" y="2" width="9" height="6.5" fill="var(--teal)"/><path d="M0.5 2 L5 5.5 L9.5 2" fill="none" stroke="var(--white)" stroke-width="0.8"/></svg>
        <span>youremail@mail.com</span>
      </li>
      <li>
        <svg viewBox="0 0 10 10" aria-hidden="true"><circle cx="5" cy="5" r="4.2" fill="none" stroke="var(--teal)" stroke-width="1"/><ellipse cx="5" cy="5" rx="1.8" ry="4.2" fill="none" stroke="var(--teal)" stroke-width="0.8"/><line x1="0.8" y1="5" x2="9.2" y2="5" stroke="var(--teal)" stroke-width="0.8"/></svg>
        <span>www.yourwebsite.com</span>
      </li>
    </ul>

    <div class="address">
      <span>address (street address<br>suite number, city, state, zip</span>
      <svg viewBox="0 0 10 13" aria-hidden="true"><path d="M5 0.5 A4.3 4.3 0 0 1 9.3 4.8 Q9.3 7.5 5 12.5 Q0.7 7.5 0.7 4.8 A4.3 4.3 0 0 1 5 0.5 Z" fill="var(--ink)"/><circle cx="5" cy="4.8" r="1.6" fill="var(--white)"/></svg>
    </div>
  </section>
</body>
</html>
```